Mirabo & Orvan Automotive Repair Shop. Need a new website design.

We specialize in Mirabo & Orvan auto repair, but also work on other Asian import vehicles. We have been in business for 7 years and pride ourselves on high quality auto repair that is fixed right the first time. Would like the automotive repair website to incorporate the colors black, red and white if possible and have our logo and some Mirabo and Orvan vehicles included in the website.

Target Market(s)

Mirabo & Orvan vehicle owners

Industry/Entity Type

Automotive Repair

Coding

Coded - Design and coding required

Number of Pages Required

5+ page

Colors
EB3D1F
EC4F4E
F09395
F8D3D4
FCEDEE

Requirements
Must have
• Home, Services, Contact Us, Schedule appointment, and a gallery tab that I can add shop pictures to when completed.
Nice to have
• Would like to see example pictures of job next to each service listed.
Should not have
• Service not related to auto repair. Ex. auto detailing, towing, car wash

```html
<!DOCTYPE html>
<html lang="en">
<head>
<meta charset="UTF-8">
<title>Kestrel Automotive</title>
<link href="https://fonts.googleapis.com/css2?family=Roboto:wght@400;500;700;900&display=swap" rel="stylesheet">
<style>
:root{
  --red:#EB1C1C;
  --red-deep:#D81515;
  --ink:#111111;
  --text:#555555;
  --grey-bg:#F2F2F4;
  --white:#FFFFFF;
  --line:#E3E3E3;
  --footer:#0D0D0D;
}
*{box-sizing:border-box;margin:0;padding:0}
html,body{width:1200px;height:3501px;overflow:hidden}
body{font-family:'Roboto',sans-serif;color:var(--ink);background:var(--white);position:relative}
.abs{position:absolute}
section{position:absolute;left:0;width:1200px;overflow:hidden}
.btn{position:absolute;background:var(--red);color:var(--white);font-size:11px;font-weight:700;display:flex;align-items:center;justify-content:center;gap:8px;text-transform:uppercase;letter-spacing:.2px}
.btn svg{width:22px;height:10px}
.rule{position:absolute;height:1px;background:var(--red)}
.photo{position:absolute}

/* hero */
.hero{top:0;height:595px;background:linear-gradient(100deg,#1b1b1b 0%,#2e2b29 40%,#5a4d44 65%,#3a3532 100%)}
.hero-photo{left:0;top:0;width:1200px;height:595px;background:radial-gradient(ellipse at 72% 40%,rgba(150,120,100,.45),rgba(0,0,0,0) 55%),linear-gradient(180deg,rgba(0,0,0,.25),rgba(0,0,0,.55))}
.nav{position:absolute;top:36px;left:113px;display:flex;gap:25px;font-size:11px;font-weight:500;color:var(--white)}
.brand{position:absolute;left:541px;top:10px;width:130px;height:108px;display:flex;flex-direction:column;align-items:center;justify-content:center;gap:6px;color:var(--white);font-weight:900;font-size:22px;letter-spacing:1px}
.brand .mark{width:26px;height:26px;background:var(--red)}
.call{position:absolute;left:757px;top:36px;font-size:11px;font-weight:500;color:var(--white);display:flex;align-items:center;gap:5px}
.book{left:956px;top:27px;width:132px;height:32px}
.hero .eyebrow{position:absolute;left:113px;top:222px;font-size:31px;font-weight:700;color:var(--red)}
.hero h1{position:absolute;left:113px;top:262px;font-size:44px;font-weight:900;color:var(--white);letter-spacing:.5px}
.hero p{position:absolute;left:113px;top:323px;width:430px;font-size:11px;line-height:19px;color:var(--white)}
.slide-arrow{position:absolute;width:42px;height:42px;border-radius:50%;background:rgba(255,255,255,.18);display:flex;align-items:center;justify-content:center}

/* about */
.about{top:595px;height:506px;background:var(--white)}
.years{position:absolute;left:447px;top:304px;width:114px;height:140px;background:var(--white);box-shadow:0 4px 18px rgba(0,0,0,.12);text-align:center}
.years b{display:block;margin-top:24px;font-size:42px;font-weight:700;color:var(--red)}
.years span{display:block;margin-top:6px;font-size:11px;line-height:19px;color:var(--red)}
.label{position:absolute;font-size:14px;color:var(--red)}
.about h2{position:absolute;left:601px;top:112px;font-size:29px;line-height:38px;font-weight:900;letter-spacing:.3px}
.about p{position:absolute;left:601px;top:275px;width:440px;font-size:11px;line-height:19px;color:var(--text)}

/* services */
.services{top:1101px;height:492px;background:var(--grey-bg)}
.sec-title{position:absolute;left:0;width:1200px;text-align:center;font-size:30px;font-weight:900;letter-spacing:.3px}
.services .intro{position:absolute;left:240px;top:103px;width:720px;text-align:center;font-size:11px;line-height:19px;color:var(--text)}
.card{position:absolute;top:197px;width:221px;height:170px;background:var(--white);border-bottom:4px solid var(--red);text-align:center}
.card .icon{position:absolute;left:76px;top:-34px;width:68px;height:68px;border-radius:50%;background:var(--white);border:1px solid var(--red);display:flex;align-items:center;justify-content:center}
.card h3{margin-top:55px;font-size:15px;font-weight:500}
.card p{margin:8px auto 0;width:180px;font-size:9.5px;line-height:12.5px;color:var(--text)}
.card a{display:block;margin-top:10px;font-size:10px;font-weight:500;color:var(--red)}
.watermark{position:absolute;left:0;width:1200px;text-align:center;font-weight:900;white-space:nowrap;letter-spacing:2px}
.services .watermark{top:390px;font-size:108px;color:rgba(0,0,0,.05)}

/* video band */
.video{top:1593px;height:302px;background:linear-gradient(90deg,#141414 0%,#2b2623 40%,#5b4e45 70%,#2c2a29 100%)}
.video .label{left:113px;top:62px;font-size:13px}
.video h2{position:absolute;left:113px;top:92px;font-size:30px;line-height:38px;font-weight:900;color:var(--white)}
.play{position:absolute;left:111px;top:179px;width:68px;height:68px;border-radius:50%;background:var(--red);box-shadow:0 0 0 8px rgba(235,28,28,.3);display:flex;align-items:center;justify-content:center}
.video .cap{position:absolute;left:193px;top:200px;font-size:8.5px;line-height:18px;font-weight:500;color:var(--white)}

/* why */
.why{top:1895px;height:473px;background:var(--white)}
.why h2{position:absolute;left:113px;top:78px;font-size:30px;font-weight:900}
.point{position:absolute;left:113px;width:340px}
.point h4{padding-left:21px;font-size:12px;font-weight:500;position:relative}
.point h4::before{content:"";position:absolute;left:0;top:3px;width:9px;height:9px;border-radius:50%;background:var(--red)}
.point p{padding-left:21px;margin-top:8px;font-size:9.5px;line-height:13px;color:var(--text)}
.counter{position:absolute;left:545px;top:272px;width:189px;height:120px;background:var(--white);border-left:3px solid var(--red);text-align:center;z-index:2}
.counter b{display:block;margin-top:24px;font-size:29px;font-weight:700;color:var(--red)}
.counter span{display:block;margin-top:4px;font-size:11px;line-height:18px;color:var(--red);font-weight:500}

/* testimonials */
.clients{top:2368px;height:356px;background:var(--red-deep)}
.clients .sec-title{top:41px;color:var(--white);font-size:30px;font-weight:700}
.clients .watermark{top:260px;font-size:110px;color:rgba(255,255,255,.12)}
.quote{position:absolute;top:106px;width:312px;height:177px;background:var(--white);z-index:2}
.quote p{position:absolute;left:26px;top:26px;width:262px;font-size:9.5px;line-height:19px;color:var(--text)}
.quote .avatar{position:absolute;left:26px;top:92px;width:52px;height:52px;border-radius:50%;background:linear-gradient(135deg,#c9b8a8,#6b5a4d)}
.quote h5{position:absolute;left:90px;top:97px;font-size:12px;font-weight:500}
.quote small{position:absolute;left:90px;top:116px;font-size:8.5px;color:var(--text)}
.quote .stars{position:absolute;left:90px;top:130px;display:flex;gap:4px}
.quote .qmark{position:absolute;right:22px;top:98px;font-size:70px;line-height:70px;font-weight:900;color:#DADADA;font-family:'Roboto',sans-serif}
.round-arrow{position:absolute;width:34px;height:34px;border-radius:50%;display:flex;align-items:center;justify-content:center;z-index:2}

/* partners */
.partners{top:2724px;height:199px;background:var(--grey-bg)}
.partner{position:absolute;top:41px;width:184px;height:117px;border:1px solid #D8D8D8;background:var(--grey-bg);display:flex;align-items:center;justify-content:center}

/* works */
.works{top:2923px;height:319px;background:var(--white)}
.works .sec-title{top:52px}
.shot{position:absolute;top:111px;width:195px;height:157px}

/* footer */
.footer{top:3242px;height:259px;background:var(--footer);color:var(--white)}
.footer .brand{left:113px;top:50px;width:126px;height:108px;font-size:20px}
.col{position:absolute;top:47px}
.col h6{font-size:15px;font-weight:700;margin-bottom:12px}
.col ul{list-style:none;font-size:9.5px;line-height:22.5px}
.sub-form{position:absolute;left:840px;top:78px;display:flex}
.sub-form .field{width:142px;height:37px;border:1px solid #777;font-size:9px;color:#ddd;padding:13px 0 0 18px}
.sub-form .go{width:100px;height:37px;background:var(--red);font-size:10px;font-weight:700;display:flex;align-items:center;justify-content:center}
.socials{position:absolute;left:840px;top:155px;display:flex;gap:8px}
.socials span{width:25px;height:25px;border-radius:50%;border:1px solid var(--white)}
.footer .divider{position:absolute;left:0;top:222px;width:1200px;height:1px;background:#444}
.footer .copy{position:absolute;left:0;top:237px;width:1200px;text-align:center;font-size:9.5px}
</style>
</head>
<body>

<section class="hero">
  <div class="photo hero-photo" role="img" aria-label="Mechanic leaning over an open engine bay in a workshop"></div>
  <nav class="nav"><span>Home</span><span>About us</span><span>Services</span><span>Blog</span><span>Contact</span></nav>
  <div class="brand"><span class="mark"></span>KESTREL</div>
  <div class="call">
    <svg width="11" height="11" viewBox="0 0 24 24"><path fill="#EB1C1C" d="M6.6 10.8a15 15 0 006.6 6.6l2.2-2.2c.3-.3.7-.4 1-.2 1.1.4 2.3.6 3.6.6.6 0 1 .4 1 1V20c0 .6-.4 1-1 1A17 17 0 013 4c0-.6.4-1 1-1h3.5c.6 0 1 .4 1 1 0 1.3.2 2.5.6 3.6.1.3 0 .7-.2 1z"/></svg>
    CALL US NOW: 555-014-2290
  </div>
  <div class="btn book">Book a Schedule</div>
  <div class="eyebrow">WELCOME TO</div>
  <h1>KESTREL AUTOMOTIVE</h1>
  <div class="rule" style="left:581px;top:286px;width:70px"></div>
  <p>Kestrel Automotive is a locally owned and operated auto repair shop in Brookfield that offers comprehensive car care and services for Mirabo &amp; Orvan and all other Asian imports vehicles.</p>
  <div class="btn" style="left:113px;top:400px;width:162px;height:40px">View All Services <svg viewBox="0 0 22 10"><path d="M0 5h20M16 1l4 4-4 4" stroke="#fff" stroke-width="1.5" fill="none"/></svg></div>
  <div class="slide-arrow" style="left:34px;top:352px"><svg width="10" height="12" viewBox="0 0 10 12"><path d="M7 1L2 6l5 5" stroke="#fff" stroke-width="1.5" fill="none"/></svg></div>
  <div class="slide-arrow" style="left:1127px;top:352px"><svg width="10" height="12" viewBox="0 0 10 12"><path d="M3 1l5 5-5 5" stroke="#fff" stroke-width="1.5" fill="none"/></svg></div>
</section>

<section class="about">
  <div class="photo" style="left:113px;top:56px;width:397px;height:348px;background:linear-gradient(160deg,#9aa3ab 0%,#4c4f55 45%,#1f2024 100%)" role="img" aria-label="Car with engine removed from its bay in a repair shop"></div>
  <div class="years"><b>20+</b><span>Years<br>Experience</span></div>
  <div class="label" style="left:601px;top:79px">About Kestrel Automotive</div>
  <h2>WE’RE PAINTLESS DENT<br>REPAIR EXPERTS DEDICATED<br>TO UNSURPASSED QUALITY,<br>SERVICE, AND RESULTS.</h2>
  <div class="rule" style="left:975px;top:243px;width:71px"></div>
  <p>Led by an NATB master certified technician with 20 years experience working for Mirabo &amp; Orvan dealerships, our auto shop is your go to facility for everything from factory auto maintenance, including oil changes, fluid services and tune ups, to complex engine repairs, hybrid diagnostic &amp; repair, brake jobs, etc.</p>
  <div class="btn" style="left:601px;top:376px;width:141px;height:40px">Read More <svg viewBox="0 0 22 10"><path d="M0 5h20M16 1l4 4-4 4" stroke="#fff" stroke-width="1.5" fill="none"/></svg></div>
</section>

<section class="services">
  <div class="rule" style="left:392px;top:63px;width:72px"></div>
  <div class="sec-title" style="top:45px">OUR SERVICES</div>
  <div class="rule" style="left:736px;top:63px;width:72px"></div>
  <p class="intro">Lorem ipsum dolor sit amet, consectetur adipiscing elit. Nullam sit amet eleifend libero. Nulla eget arcu tempus, congue ex ut, aliquam odio. Vestibulum id fringilla lectus.</p>
  <div class="watermark">KESTREL AUTOMOTIVE</div>

  <div class="card" style="left:113px">
    <div class="icon"><svg width="30" height="30" viewBox="0 0 24 24"><path fill="#EB1C1C" d="M12 2s7 8 7 13a7 7 0 01-14 0c0-5 7-13 7-13z"/><circle cx="9.5" cy="15" r="2" fill="#fff"/></svg></div>
    <h3>Oil Changes</h3>
    <p>A regular oil change is one of best forms of routine maintenance you can perform on your vehicle.</p>
    <a>Read More +</a>
  </div>
  <div class="card" style="left:364px">
    <div class="icon"><svg width="30" height="30" viewBox="0 0 24 24"><rect x="2" y="3" width="20" height="13" fill="#EB1C1C"/><rect x="9" y="17" width="6" height="2" fill="#EB1C1C"/><rect x="6" y="19" width="12" height="2" fill="#EB1C1C"/></svg></div>
    <h3>Computer Diagnostics</h3>
    <p>However these new computer systems are not without their own set of drawbacks.</p>
    <a>Read More +</a>
  </div>
  <div class="card" style="left:615px">
    <div class="icon"><svg width="30" height="30" viewBox="0 0 24 24"><path fill="#EB1C1C" d="M14 1L4 14h7l-2 9 10-13h-7z"/></svg></div>
    <h3>Electrical Specialists</h3>
    <p>Electronics play an enormous role in the proper function, and the comfort of your motor vehicle.</p>
    <a>Read More +</a>
  </div>
  <div class="card" style="left:866px">
    <div class="icon"><svg width="30" height="30" viewBox="0 0 24 24"><path d="M4 4l16 16M20 4L4 20" stroke="#EB1C1C" stroke-width="3" stroke-linecap="round"/><circle cx="5" cy="5" r="3" fill="none" stroke="#EB1C1C" stroke-width="2"/></svg></div>
    <h3>Engine Repair</h3>
    <p>Having a major problem? Not a problem. Torque Line is equipped to handle all types of engine repair.</p>
    <a>Read More +</a>
  </div>

  <div class="btn" style="left:519px;top:394px;width:162px;height:41px">View All Services <svg viewBox="0 0 22 10"><path d="M0 5h20M16 1l4 4-4 4" stroke="#fff" stroke-width="1.5" fill="none"/></svg></div>
</section>

<section class="video">
  <div class="photo" style="left:0;top:0;width:1200px;height:302px;background:radial-gradient(ellipse at 68% 45%,rgba(170,135,110,.45),rgba(0,0,0,0) 55%)" role="img" aria-label="Mechanic working under a car with a work light"></div>
  <div class="label">Working since 1992</div>
  <h2>WE ARE LEADER<br>IN CAR MECHANICAL</h2>
  <div class="rule" style="left:455px;top:149px;width:70px"></div>
  <div class="play"><svg width="18" height="20" viewBox="0 0 18 20"><path d="M2 1l15 9-15 9z" fill="#fff"/></svg></div>
  <div class="cap">WATCH INTRO VIDEO<br>ABOUT US</div>
</section>

<section class="why">
  <h2>WHY CHOOSE</h2>
  <div class="rule" style="left:346px;top:94px;width:70px"></div>
  <div class="point" style="top:141px"><h4>We Make It Easy</h4><p>Get a quote and book a service online 24/7. Our mechanics will come to your home or office, even on evenings and weekends.</p></div>
  <div class="point" style="top:204px"><h4>Fair And Transparent Pricing</h4><p>We offer fair and transparent pricing and provide estimates upfront for hundreds of services on thousands of cars. Book with confidence.</p></div>
  <div class="point" style="top:267px"><h4>Backed By Warranty</h4><p>We only work with highly rated mechanics.All services are backed by our 12-month / 12,000-mile warranty.</p></div>
  <div class="btn" style="left:113px;top:332px;width:141px;height:41px">Read More <svg viewBox="0 0 22 10"><path d="M0 5h20M16 1l4 4-4 4" stroke="#fff" stroke-width="1.5" fill="none"/></svg></div>
  <div class="photo" style="left:662px;top:63px;width:209px;height:348px;background:linear-gradient(170deg,#a9b3bb 0%,#4d5156 55%,#1c1d20 100%)" role="img" aria-label="Sedan with its hood open in a garage"></div>
  <div class="photo" style="left:878px;top:63px;width:209px;height:348px;background:linear-gradient(170deg,#8e8a84 0%,#5c5248 50%,#2a2522 100%)" role="img" aria-label="Mechanic repairing the underside of a lifted car"></div>
  <div class="counter"><b>5625+</b><span>Customers Happy with Our<br>Services</span></div>
</section>

<section class="clients">
  <div class="rule" style="left:404px;top:58px;width:72px;background:#fff"></div>
  <div class="sec-title">What Our Clients Say</div>
  <div class="rule" style="left:766px;top:58px;width:72px;background:#fff"></div>
  <div class="watermark">KESTREL AUTOMOTIVE</div>
  <div class="round-arrow" style="left:58px;top:186px;background:#fff"><svg width="8" height="10" viewBox="0 0 8 10"><path d="M6 1L2 5l4 4" stroke="#111" stroke-width="1.3" fill="none"/></svg></div>
  <div class="round-arrow" style="left:1108px;top:186px;border:1px solid #fff"><svg width="8" height="10" viewBox="0 0 8 10"><path d="M2 1l4 4-4 4" stroke="#fff" stroke-width="1.3" fill="none"/></svg></div>

  <div class="quote" style="left:113px">
    <p>Lorem ipsum dolor sit amet, consectetur adipiscing elit. Maecenas eget metus mattis leo accumsan imperdiet vel elementum tellus.</p>
    <div class="avatar" role="img" aria-label="Client portrait"></div>
    <h5>Dana Holt</h5><small>Managing Director</small>
    <div class="stars"><svg width="78" height="10" viewBox="0 0 78 10"><g fill="#F5B400"><path id="s" d="M5 0l1.5 3.2L10 3.6 7.4 6l.7 3.5L5 7.8 1.9 9.5 2.6 6 0 3.6l3.5-.4z"/><use href="#s" x="17"/><use href="#s" x="34"/><use href="#s" x="51"/><use href="#s" x="68"/></g></svg></div>
    <div class="qmark">”</div>
  </div>
  <div class="quote" style="left:445px">
    <p>Lorem ipsum dolor sit amet, consectetur adipiscing elit. Maecenas eget metus mattis leo accumsan imperdiet vel elementum tellus.</p>
    <div class="avatar" role="img" aria-label="Client portrait"></div>
    <h5>Dana Holt</h5><small>Managing Director</small>
    <div class="stars"><svg width="78" height="10" viewBox="0 0 78 10"><g fill="#F5B400"><use href="#s"/><use href="#s" x="17"/><use href="#s" x="34"/><use href="#s" x="51"/><use href="#s" x="68"/></g></svg></div>
    <div class="qmark">”</div>
  </div>
  <div class="quote" style="left:775px">
    <p>Lorem ipsum dolor sit amet, consectetur adipiscing elit. Maecenas eget metus mattis leo accumsan imperdiet vel elementum tellus.</p>
    <div class="avatar" role="img" aria-label="Client portrait"></div>
    <h5>Dana Holt</h5><small>Managing Director</small>
    <div class="stars"><svg width="78" height="10" viewBox="0 0 78 10"><g fill="#F5B400"><use href="#s"/><use href="#s" x="17"/><use href="#s" x="34"/><use href="#s" x="51"/><use href="#s" x="68"/></g></svg></div>
    <div class="qmark">”</div>
  </div>
</section>

<section class="partners">
  <div class="partner" style="left:113px"><svg width="100" height="40"><rect x="10" y="8" width="80" height="24" rx="3" fill="#D93A2B"/></svg></div>
  <div class="partner" style="left:311px"><svg width="100" height="40"><rect x="5" y="12" width="90" height="16" fill="#E02424"/></svg></div>
  <div class="partner" style="left:509px"><svg width="100" height="70"><circle cx="50" cy="35" r="30" fill="none" stroke="#3A78C2" stroke-width="4"/></svg></div>
  <div class="partner" style="left:706px"><svg width="110" height="40"><rect x="5" y="10" width="100" height="20" rx="10" fill="#2BA84A"/></svg></div>
  <div class="partner" style="left:904px"><svg width="90" height="90"><circle cx="45" cy="45" r="38" fill="#1F5FB0"/></svg></div>
</section>

<section class="works">
  <div class="rule" style="left:420px;top:70px;width:72px"></div>
  <div class="sec-title">OUR WORKS</div>
  <div class="rule" style="left:713px;top:70px;width:72px"></div>
  <div class="shot" style="left:0;background:linear-gradient(150deg,#8e949a,#3a3d42)" role="img" aria-label="Engine repair in progress"></div>
  <div class="shot" style="left:206px;background:linear-gradient(150deg,#7e7668,#2f2b27)" role="img" aria-label="Engine block on a stand"></div>
  <div class="shot" style="left:412px;background:linear-gradient(150deg,#b9b4ac,#55504a)" role="img" aria-label="Car raised on a lift in the shop"></div>
  <div class="shot" style="left:618px;background:linear-gradient(150deg,#9a9590,#3b3835)" role="img" aria-label="Brake disc and clutch parts"></div>
  <div class="shot" style="left:824px;background:linear-gradient(150deg,#8c96a6,#2e3644)" role="img" aria-label="Vehicle on a blue lift in service bay"></div>
  <div class="shot" style="left:1030px;background:linear-gradient(150deg,#a5a09a,#4a4540)" role="img" aria-label="Mechanic working on suspension"></div>
</section>

<footer class="footer" style="position:absolute;left:0;width:1200px">
  <div class="brand"><span class="mark"></span>KESTREL</div>
  <div class="col" style="left:332px"><h6>Explore</h6><ul><li>About Us</li><li>Popular Services</li><li>Why Choose Us</li><li>Portfolio</li><li>Contact Us</li></ul></div>
  <div class="col" style="left:496px"><h6>Our Services</h6><ul><li>Oil Changes</li><li>Computer Diagnostics</li><li>Electrical Specialists</li><li>Tires</li><li>Tire Balance &amp; Rotations</li></ul></div>
  <div class="col" style="left:674px;top:72px"><ul style="line-height:22.5px"><li>Pre Purchase Inspections</li><li>Insurance Claims</li><li style="line-height:12px;padding:5px 0">Emission Repair &amp; Catalytic<br>Converters</li><li>Engine Repair</li><li>Heating &amp; AC Repair</li></ul></div>
  <div class="col" style="left:840px"><h6 style="font-size:17px">Subscribe To Our Newsletter</h6></div>
  <div class="sub-form"><div class="field">Enter your email</div><div class="go">SUBSCRIBE</div></div>
  <div class="abs" style="left:840px;top:135px;font-size:9.5px">Follow Us:</div>
  <div class="socials"><span></span><span></span><span></span><span></span></div>
  <div class="divider"></div>
  <div class="copy">Copyright © 2024. All rights reserved.</div>
</footer>

</body>
</html>
```